Korean Homemade food restaurant just like what your mom cooks at home

I need a black and white simple and modern design according to my logo.
My restaurant name is Noru Kan (meaning of home cooking).
I need to have 솔찬(Noru Kan) in Korean need to be included. Once again 솔찬.
I am not sure if I need to include my name and number and adress.

솔찬 Noru Kan 418 Marlow Ct. Clarksville, TN 37512 Grant Oh Owner Cell:931-555-0183 Store:931-555-0297

Target Market(s)

business owners, university students

Industry/Entity Type

Restaurant

Contact Information for Business Card

This is traditional Korean food restaurant that targets university students during lunch and Korean business travelers at dinner.

Font styles to use
Sans Serif

Requirements
Must have
• Must have my logo.

```html
<!DOCTYPE html>
<html lang="en">
<head>
<meta charset="utf-8">
<title>Noru Kan – Business Card</title>
<link rel="stylesheet" href="https://fonts.googleapis.com/css2?family=Jost:wght@500&family=Noto+Sans+KR:wght@700&family=Kalam:wght@400&display=swap">
<style>
  :root {
    --stage: #e9ebeb;
    --card: #ffffff;
    --ink: #2b2a29;
    --paper-text: #ffffff;
    --art-tone: #bdbdbd;
    --shadow: rgba(0, 0, 0, 0.12);
  }
  * { box-sizing: border-box; margin: 0; padding: 0; }
  html, body {
    width: 1013px;
    height: 1200px;
    overflow: hidden;
    background: var(--stage);
  }
  .stage {
    position: relative;
    width: 1013px;
    height: 1200px;
  }
  .card {
    position: absolute;
    width: 754px;
    height: 448px;
    background: var(--card);
    border-radius: 46px;
    overflow: hidden;
    box-shadow: 0 4px 18px var(--shadow);
  }
  .card--front { left: 143px; top: 126px; }
  .card--back  { left: 131px; top: 638px; }

  .band {
    position: absolute;
    left: 0;
    width: 100%;
    background: var(--ink);
    display: flex;
    align-items: center;
    justify-content: center;
  }
  .card--front .band { top: 300px; height: 148px; }
  .card--back .band  { top: 0; height: 148px; }

  .korean-name {
    font-family: "Noto Sans KR", sans-serif;
    font-weight: 700;
    font-size: 74px;
    line-height: 1;
    color: var(--paper-text);
    letter-spacing: 2px;
  }
  .card--front .korean-name { margin-top: 38px; }

  .art {
    position: absolute;
    background: var(--art-tone);
    border-radius: 6px;
  }
  .art--mark     { left: 298px; top: 37px; width: 165px; height: 169px; border-radius: 50% 50% 8px 8px; }
  .art--cutlery-left  { left: 17px;  top: 271px; width: 116px; height: 58px; }
  .art--cutlery-right { left: 612px; top: 270px; width: 116px; height: 58px; background: #d9d9d9; }
  .art--cutlery-back  { left: 312px; top: 177px; width: 116px; height: 60px; }

  .wordmark {
    position: absolute;
    left: 0;
    top: 196px;
    width: 100%;
    text-align: center;
    font-family: "Jost", sans-serif;
    font-weight: 500;
    font-size: 74px;
    line-height: 1;
    color: var(--ink);
  }

  .contact {
    position: absolute;
    left: 0;
    width: 100%;
    text-align: center;
    font-family: "Kalam", cursive;
    color: var(--ink);
    line-height: 1;
  }
  .contact--phone   { top: 270px; font-size: 35px; }
  .contact--address { top: 334px; font-size: 31px; }
</style>
</head>
<body>
<main class="stage">
  <section class="card card--front">
    <div class="art art--mark" role="img" aria-label="Restaurant symbol area"></div>
    <p class="wordmark">Noru Kan</p>
    <div class="art art--cutlery-left" role="img" aria-label="Spoon and chopsticks illustration"></div>
    <div class="art art--cutlery-right" role="img" aria-label="Spoon and chopsticks illustration"></div>
    <div class="band">
      <p class="korean-name" lang="ko">솔찬</p>
    </div>
  </section>

  <section class="card card--back">
    <div class="band">
      <p class="korean-name" lang="ko">솔찬</p>
    </div>
    <div class="art art--cutlery-back" role="img" aria-label="Spoon and chopsticks illustration"></div>
    <p class="contact contact--phone">931-555-0183</p>
    <p class="contact contact--address">418 Marlow Ct. Clarksville TN 37512</p>
  </section>
</main>
</body>
</html>
```